Create/Design Awesome VornaMD Label for Pain Cream

I need a label design for a pain relief cream to be sold online in a highly competitve space(brindle). Therefore the label needs to be a killer and really jump off the page.
I am a RN so I want it to have a bit of a clinical look while still embracing an all natural product (blend east & west medicine?). It will be on a small solid white tub (3oz). The look should communicate pain alleviation/relief, all natural feel good, cooling soothing. The product color is like azure/light blue so may could incorporate that.

You can view the competition here: https://www.brindlemart.example/s/ref=nb_sb_ss_i_2_5?url=search-alias%3Daps&field-keywords=pain+relief+cream&sprefix=pain+%2Caps%2C163

You can see some of my other products here: http://www.brindlemart.example/s?marketplaceID=QLM3TRWZP8HUY&me=KJD2H9B4XQTRW&merchant=KJD2H9B4XQTRW&redirect=true

VornaMD All Natural
Pain Relief
Inflammation
Formulation

with Arnica, B6 & MSM

This should be wording on front of label. May rearrange or add to? Can use template boxes on sides.

PS: Hoping on creative & patient designer who can help me make this really awesome. Looking for long term relationship as I have many other products in the works.
Updates

Think clinical/professional but still friendly. Like something your doctor od pharmacist may give you. Added Sunday, December 6, 2015

Reason: I was just now able to complete brief with more information. Want to give ample time for best designs.

Target Market(s)

35-90 years old, male and females

Industry/Entity Type

Medical

Colors
85acd3
3377b5
fbee3f
fbed22
ec1f27
ffffff
9bcb3c

Requirements
Must have
• Bright, colorful, clinical all natural look.
Nice to have
• maybe some images of musculo-sketekal (spine, Knees, elbows) in background?
Should not have
• Please do not copy front wording of template

```html
<!DOCTYPE html>
<html lang="en">
<head>
<meta charset="utf-8">
<title>VornaMD Pain Relief Label</title>
<link rel="stylesheet" href="https://fonts.googleapis.com/css2?family=Open+Sans:ital,wght@0,400;0,600;0,700;1,400&display=swap">
<style>
  :root {
    --bg: #f4f6f8;
    --label-edge: #8fc0e6;
    --label-mid: #bfe0f7;
    --label-glow: #eef7fd;
    --panel-line: #3a6f9c;
    --ink: #1a1a1a;
  }
  * { box-sizing: border-box; margin: 0; padding: 0; }
  html, body { width: 1200px; height: 1000px; overflow: hidden; }
  body {
    background: var(--bg);
    font-family: "Open Sans", Arial, sans-serif;
    color: var(--ink);
    position: relative;
  }
  .label {
    position: absolute;
    left: 40px; top: 200px;
    width: 1120px; height: 600px;
    display: flex;
    background: radial-gradient(ellipse 40% 70% at 50% 55%, var(--label-glow) 0%, var(--label-mid) 60%, var(--label-edge) 100%);
    box-shadow: 0 4px 18px rgba(0,0,0,.12);
  }
  .side-panel {
    width: 290px;
    padding: 40px 22px;
    font-size: 10.5px;
    line-height: 1.45;
  }
  .facts-box {
    border: 1.5px solid var(--panel-line);
    padding: 10px 12px;
    height: 100%;
    background: rgba(255,255,255,.25);
  }
  .facts-title { font-weight: 700; font-size: 14px; border-bottom: 2px solid var(--panel-line); padding-bottom: 3px; margin-bottom: 6px; }
  .facts-row { display: flex; justify-content: space-between; border-bottom: 1px solid var(--panel-line); padding: 2px 0; }
  .facts-head { font-weight: 700; margin-top: 6px; }
  .facts-box p { margin-bottom: 4px; }
  .front-panel {
    flex: 1;
    text-align: center;
    padding-top: 70px;
  }
  .maker { font-size: 22px; letter-spacing: .5px; }
  .product-name {
    color: var(--ink);
    font-weight: 400;
    font-size: 92px;
    line-height: 1.2;
    letter-spacing: 0;
    margin-top: 38px;
  }
  .claim { font-size: 35px; margin-top: 8px; letter-spacing: -.3px; }
  .category { font-size: 24px; margin-top: 40px; }
  .ingredients { font-size: 16px; font-style: italic; margin-top: 2px; }
  .net-weight { font-size: 22px; margin-top: 64px; }
</style>
</head>
<body>
  <main class="label">
    <section class="side-panel">
      <div class="facts-box">
        <div class="facts-title">Drug Facts</div>
        <div class="facts-row"><strong>Active ingredients</strong><strong>Purpose</strong></div>
        <div class="facts-row"><span>Menthol 2%</span><span>Topical analgesic</span></div>
        <div class="facts-head">Uses</div>
        <p>Temporarily relieves minor aches and pains of muscles and joints associated with simple backache, strains, bruises and sprains.</p>
        <div class="facts-head">Warnings</div>
        <p>For external use only. Keep away from excessive heat or flame.</p>
        <p>When using this product avoid contact with eyes and mucous membranes. Do not apply to wounds or damaged skin.</p>
        <p>Stop use and ask a doctor if condition worsens or symptoms persist for more than 7 days.</p>
        <p>Made for Meridale Labs, Springfield</p>
      </div>
    </section>

    <section class="front-panel">
      <div class="maker">MERIDALE LABS</div>
      <h1 class="product-name">VornaMD</h1>
      <div class="claim">ALL NATURAL PAIN RELIEF</div>
      <div class="category">Topical Analgesic</div>
      <div class="ingredients">With Arnica, B6 &amp; Msm</div>
      <div class="net-weight">Net Wt. 3 oz. (85g)</div>
    </section>

    <section class="side-panel">
      <div class="facts-box">
        <div class="facts-title">Drug Facts (continued)</div>
        <p>If pregnant or breast-feeding, ask a health professional before use.</p>
        <p>Keep out of reach of children.</p>
        <div class="facts-head">Directions</div>
        <p>Adults and children 12 years and older: apply to affected area up to 3 to 4 times daily.</p>
        <p>Children under 12: ask a doctor.</p>
        <p><strong>Other information</strong> store at room temperature.</p>
        <p><strong>Inactive ingredients</strong> water, aloe vera, arnica montana, MSM, pyridoxine, glycerin, carbomer.</p>
      </div>
    </section>
  </main>
</body>
</html>
```